STI/STD Medical Clinic- Wellspring Crest Partners, Inc Website

We are a STI clinic in florida looking for a website. We want to be professional but also playful. We want a buildout similar to the website listed below as our clinic is very similar to theirs.

This is a great example of a clinic doing similar stuff as us. We obviously do not want their color scheme but their format and buildout work. Please see our logo attached for color schemes etc.

https://bluefernclinicmiami.org

Industry/Entity Type

Medical

Coding

Coded - Design and coding required

Number of Pages Required

5+ page

Font styles to use
Sans Serif

```html
<!DOCTYPE html>
<html lang="en">
<head>
<meta charset="utf-8">
<title>Wellspring Crest Partners, Inc</title>
<link href="https://fonts.googleapis.com/css2?family=Poppins:wght@400;500;600;700&display=swap" rel="stylesheet">
<style>
:root{
  --pink:#f2467a;
  --pink-2:#ff6f61;
  --blue:#3a3cf0;
  --navy:#17176c;
  --ink:#222230;
  --muted:#6d6d7c;
  --line:#e6e6ee;
  --white:#fff;
}
*{box-sizing:border-box;margin:0;padding:0}
html,body{width:1200px;height:3960px;overflow:hidden}
body{font-family:'Poppins',sans-serif;color:var(--ink);background:var(--white);position:relative}
.section{position:absolute;left:0;width:1200px}
.btn{display:inline-block;background:linear-gradient(90deg,var(--pink),var(--pink-2));color:#fff;font-size:14px;font-weight:500;padding:10px 26px;border-radius:6px}
.brand{display:flex;align-items:center;gap:10px;font-weight:700;font-size:18px;color:var(--blue)}
.brand-dot{width:34px;height:34px;border-radius:50%;background:var(--pink)}

/* header */
.site-header{top:0;height:60px;background:#fff;display:flex;align-items:center;padding:0 150px;box-shadow:0 2px 8px rgba(0,0,0,.08);z-index:2}
.main-nav{display:flex;gap:8px;margin-left:auto;margin-right:24px}
.main-nav a{font-size:13px;padding:7px 14px;color:var(--ink);text-decoration:none}
.main-nav a.active{background:var(--pink);color:#fff}
.phone-pill{display:flex;align-items:center;gap:8px;background:var(--pink);color:#fff;font-size:13px;padding:7px 16px;border-radius:20px}

/* hero */
.hero{top:60px;height:540px;background:linear-gradient(180deg,#3c4a4c,#6b7470 55%,#3b3d40)}
.hero-shade{position:absolute;inset:0;background:rgba(20,24,30,.35)}
.hero-copy{position:absolute;top:230px;width:100%;text-align:center;color:#fff}
.hero-copy h1{font-size:50px;line-height:1.2;font-weight:700}
.hero-copy h1 span{color:var(--pink)}
.hero-copy p{font-size:24px;margin:12px 0 24px}
.hero-arrow{position:absolute;top:250px;width:30px;height:40px}
.hero-arrow.prev{left:20px}.hero-arrow.next{right:20px}

/* clinic */
.clinic{top:600px;height:460px}
.clinic-art{position:absolute;left:150px;top:80px;width:320px;height:320px;border-radius:50%;background:radial-gradient(circle,#fff 30%,#c6c3ff 60%,#f7a9d0 100%)}
.clinic-copy{position:absolute;left:600px;top:120px;width:380px}
.section-title{font-size:26px;font-weight:700;letter-spacing:.5px}
.clinic-copy p{font-size:13px;color:var(--muted);line-height:1.7;margin:14px 0 20px}

/* services */
.services{top:1060px;height:680px;background:var(--blue);color:#fff}
.services .section-title{text-align:center;margin-top:76px}
.title-rule{width:60px;height:3px;background:#fff;margin:10px auto 0}
.services .lead{text-align:center;font-size:13px;opacity:.85;line-height:1.7;margin:18px auto 0;width:360px}
.service-grid{position:absolute;left:140px;top:250px;width:930px;display:grid;grid-template-columns:repeat(3,310px);row-gap:90px}
.service{display:flex;gap:14px;padding:20px 20px 24px;width:290px;border-radius:6px}
.service.featured{background:linear-gradient(160deg,var(--pink),var(--pink-2));margin-top:-20px}
.service-icon{flex:none;width:44px;height:44px;border-radius:50%;background:var(--pink);display:flex;align-items:center;justify-content:center}
.service.featured .service-icon{background:#fff}
.service h3{font-size:17px;font-weight:600;margin-bottom:6px;white-space:nowrap}
.service p{font-size:12px;line-height:1.6;opacity:.9}

/* faq */
.faq{top:1740px;height:340px}
.faq .section-title{text-align:center;margin-top:66px}
.faq-grid{position:absolute;left:150px;top:130px;width:900px;display:grid;grid-template-columns:repeat(3,1fr);gap:24px 36px}
.faq-item{position:relative;background:#fff;box-shadow:0 2px 10px rgba(0,0,0,.1);font-size:12px;padding:12px 14px;line-height:1.5}
.faq-item.open{background:var(--pink);color:#fff}
.faq-answer{font-size:11px;color:var(--muted);line-height:1.6;padding:10px 14px 0}
.faq-toggle{position:absolute;top:-8px;right:-8px;width:18px;height:18px;border-radius:50%;background:var(--pink);color:#fff;font-size:13px;line-height:18px;text-align:center}

/* appointment */
.appointment{top:2080px;height:540px}
.appointment-band{position:absolute;left:40px;right:0;top:0;height:540px;background:var(--blue);border-radius:270px 0 0 270px}
.appointment-art{position:absolute;left:80px;top:60px;width:400px;height:420px;border-radius:50%;background:radial-gradient(circle,#fff 20%,#9fb0ff 70%,var(--blue) 100%);opacity:.9}
.appointment-form{position:absolute;left:515px;top:70px;width:530px;color:#fff}
.form-row{display:grid;grid-template-columns:1fr 1fr;gap:12px;margin-top:12px}
.field{background:#fff;border-radius:6px;height:40px;color:#888;font-size:13px;padding:10px 14px}
.field.message{height:110px;margin-top:12px}
.appointment-form .btn{margin-top:14px}

/* news */
.news{top:2620px;height:480px}
.news .section-title{text-align:center;margin-top:16px}
.news-grid{position:absolute;left:150px;top:80px;width:900px;display:grid;grid-template-columns:repeat(3,1fr);gap:20px}
.news-card{box-shadow:0 2px 10px rgba(0,0,0,.1);background:#fff}
.news-photo{height:230px;background:linear-gradient(160deg,#c9d3d8,#eef1f2 50%,#b3c2c9)}
.news-body{padding:14px;border-bottom:4px solid var(--pink)}
.news-meta{font-size:10px;color:var(--muted)}
.news-body h4{font-size:17px;font-weight:500;line-height:1.35;margin-top:6px}
.news .btn{position:absolute;left:540px;top:410px}

/* partners */
.partners{top:3100px;height:340px;border-top:1px solid var(--line)}
.partners .section-title{text-align:center;margin-top:110px}
.partner-row{position:absolute;top:200px;left:170px;width:860px;display:flex;justify-content:space-between;align-items:center}
.partner-mark{width:110px;height:28px;border-radius:4px;background:#c9c9d3}

/* footer */
.site-footer{top:3440px;height:520px;background:var(--navy);color:#fff}
.footer-cols{position:absolute;left:150px;top:110px;width:900px;display:grid;grid-template-columns:1.1fr 1fr 1.1fr 1.1fr;gap:30px}
.site-footer h5{font-size:15px;font-weight:600;margin-bottom:18px}
.site-footer p,.site-footer li{font-size:12px;line-height:1.8;opacity:.85;list-style:none}
.contact-line{display:flex;gap:8px;margin-bottom:10px;font-size:12px;opacity:.85}
.contact-line svg{flex:none;margin-top:3px}
.site-footer li::before{content:"";display:inline-block;width:6px;height:6px;background:var(--pink);border-radius:50%;margin-right:8px}
.news-input{background:#fff;color:#888;font-size:12px;padding:10px 12px;border-radius:4px;margin:12px 0 10px}
.socials{position:absolute;top:380px;left:0;width:100%;display:flex;justify-content:center;gap:12px}
.socials span{width:28px;height:28px;border-radius:50%;background:var(--pink)}
.footer-rule{position:absolute;top:432px;left:150px;width:900px;height:1px;background:rgba(255,255,255,.2)}
.copyright{position:absolute;top:460px;width:100%;text-align:center;font-size:12px;opacity:.75}
</style>
</head>
<body>

<header class="section site-header">
  <div class="brand"><span class="brand-dot"></span>Wellspring Crest</div>
  <nav class="main-nav">
    <a class="active">Home</a><a>About</a><a>Services</a><a>News</a><a>Contact</a>
  </nav>
  <div class="phone-pill">
    <svg width="14" height="14" viewBox="0 0 24 24"><path fill="#fff" d="M6.6 10.8a15 15 0 0 0 6.6 6.6l2.2-2.2c.3-.3.7-.4 1-.2 1.1.4 2.3.6 3.6.6.6 0 1 .4 1 1V20c0 .6-.4 1-1 1A17 17 0 0 1 3 4c0-.6.4-1 1-1h3.5c.6 0 1 .4 1 1 0 1.3.2 2.5.6 3.6.1.3 0 .7-.2 1z"/></svg>
    321-555-0142
  </div>
</header>

<section class="section hero">
  <div class="hero-shade" role="img" aria-label="Photo of the clinic reception room"></div>
  <svg class="hero-arrow prev" viewBox="0 0 30 40"><path d="M22 4 6 20l16 16" fill="none" stroke="#fff" stroke-width="3"/></svg>
  <svg class="hero-arrow next" viewBox="0 0 30 40"><path d="M8 4l16 16L8 36" fill="none" stroke="var(--pink)" stroke-width="3"/></svg>
  <div class="hero-copy">
    <h1>We Are Wellspring Crest<br>Partners In <span>Florida</span></h1>
    <p>Bridging the gaps in improve the health of our community</p>
    <a class="btn">Contact Us</a>
  </div>
</section>

<section class="section clinic">
  <div class="clinic-art" role="img" aria-label="Colourful knotted ribbon illustration"></div>
  <div class="clinic-copy">
    <h2 class="section-title">MEET OUR CLINIC</h2>
    <p>There are many variations of passages of Lorem Ipsum available, but the majority have suffered alteration in some form, by injected humour, or randomised words which don't look even slightly believable. If you are going to use a passage of Lorem Ipsum, you need.</p>
    <a class="btn">About Us</a>
  </div>
</section>

<section class="section services">
  <h2 class="section-title">SERVICES</h2>
  <div class="title-rule"></div>
  <p class="lead">It is a long established fact that a reader will be distracted by the readable content</p>
  <div class="service-grid">
    <div class="service"><span class="service-icon"><svg width="20" height="20" viewBox="0 0 24 24"><circle cx="12" cy="12" r="7" fill="none" stroke="#fff" stroke-width="2"/><path d="M12 8v8M8 12h8" stroke="#fff" stroke-width="2"/></svg></span><div><h3>PrEP</h3><p>There are many variations of passages of Lorem Ipsum available.</p></div></div>
    <div class="service featured"><span class="service-icon"><svg width="20" height="20" viewBox="0 0 24 24"><path d="M6 4v7a6 6 0 0 0 12 0V4" fill="none" stroke="var(--pink)" stroke-width="2"/><circle cx="18" cy="17" r="2" fill="var(--pink)"/></svg></span><div><h3>PeP</h3><p>There are many variations of passages of Lorem Ipsum available.</p></div></div>
    <div class="service"><span class="service-icon"><svg width="20" height="20" viewBox="0 0 24 24"><path d="M12 3c4 5 6 8 6 11a6 6 0 0 1-12 0c0-3 2-6 6-11z" fill="#fff"/></svg></span><div><h3>Hepatitis C</h3><p>There are many variations of passages of Lorem Ipsum available.</p></div></div>
    <div class="service"><span class="service-icon"><svg width="20" height="20" viewBox="0 0 24 24"><path d="M12 4c-3 0-4 4-2 7l6 9M12 4c3 0 4 4 2 7l-6 9" fill="none" stroke="#fff" stroke-width="2"/></svg></span><div><h3>HIV</h3><p>There are many variations of passages of Lorem Ipsum available.</p></div></div>
    <div class="service"><span class="service-icon"><svg width="20" height="20" viewBox="0 0 24 24"><circle cx="12" cy="12" r="5" fill="#fff"/><path d="M12 2v4M12 18v4M2 12h4M18 12h4" stroke="#fff" stroke-width="2"/></svg></span><div><h3>STI</h3><p>There are many variations of passages of Lorem Ipsum available.</p></div></div>
    <div class="service"><span class="service-icon"><svg width="20" height="20" viewBox="0 0 24 24"><rect x="5" y="4" width="14" height="17" rx="2" fill="none" stroke="#fff" stroke-width="2"/><path d="M9 10h6M9 14h6" stroke="#fff" stroke-width="2"/></svg></span><div><h3>Case Management</h3><p>There are many variations of passages of Lorem Ipsum available.</p></div></div>
  </div>
</section>

<section class="section faq">
  <h2 class="section-title">FREQUENTLY ASKED QUESTIONS</h2>
  <div class="faq-grid">
    <div>
      <div class="faq-item">Long established fact that a reader will be distracted.<span class="faq-toggle">+</span></div>
      <div class="faq-item" style="margin-top:24px">Long established fact that a reader will be distracted.<span class="faq-toggle">+</span></div>
    </div>
    <div>
      <div class="faq-item open">Long established fact that a reader will be distracted.<span class="faq-toggle">−</span></div>
      <p class="faq-answer">Many desktop publishing packages and web page editors now use Lorem Ipsum as their default model text, and a search for.</p>
    </div>
    <div>
      <div class="faq-item">Long established fact that a reader will be distracted.<span class="faq-toggle">+</span></div>
      <div class="faq-item" style="margin-top:24px">Long established fact that a reader will be distracted.<span class="faq-toggle">+</span></div>
    </div>
  </div>
</section>

<section class="section appointment">
  <div class="appointment-band"></div>
  <div class="appointment-art" role="img" aria-label="White knotted ribbon illustration"></div>
  <form class="appointment-form">
    <h2 class="section-title">MAKE AN APPOINTMENT</h2>
    <div class="form-row" style="margin-top:20px"><div class="field">First Name</div><div class="field">Last Name</div></div>
    <div class="form-row"><div class="field">Email</div><div class="field">Phone</div></div>
    <div class="field message">Message</div>
    <a class="btn">Submit Now</a>
  </form>
</section>

<section class="section news">
  <h2 class="section-title">NEWS</h2>
  <div class="news-grid">
    <article class="news-card"><div class="news-photo" role="img" aria-label="Photo of a doctor consulting with a patient"></div><div class="news-body"><div class="news-meta">MAY 18, 2022 · BY LOREM IPSUM</div><h4>Lorem Ipsum is simply dummy text of the printing</h4></div></article>
    <article class="news-card"><div class="news-photo" role="img" aria-label="Photo of a medical team in a hallway"></div><div class="news-body"><div class="news-meta">MAY 18, 2022 · BY LOREM IPSUM</div><h4>Lorem Ipsum is simply dummy text of the printing</h4></div></article>
    <article class="news-card"><div class="news-photo" role="img" aria-label="Photo of nurses caring for a patient"></div><div class="news-body"><div class="news-meta">MAY 18, 2022 · BY LOREM IPSUM</div><h4>Lorem Ipsum is simply dummy text of the printing</h4></div></article>
  </div>
  <a class="btn">View All</a>
</section>

<section class="section partners">
  <h2 class="section-title">PARTNER</h2>
  <div class="partner-row">
    <span class="partner-mark"></span><span class="partner-mark"></span><span class="partner-mark"></span><span class="partner-mark"></span><span class="partner-mark"></span>
  </div>
</section>

<footer class="section site-footer">
  <div class="footer-cols">
    <div>
      <div class="brand" style="color:#fff;margin-bottom:18px"><span class="brand-dot"></span>Wellspring Crest</div>
      <p>Lorem ipsum dolor sit amet, consectetur adipiscing elit, sed do eiusmod tempor.</p>
      <p style="margin-top:8px">Lorem ipsum dolor sit amet, consectetur adipiscing.</p>
    </div>
    <div>
      <h5>CONTACT</h5>
      <div class="contact-line"><svg width="12" height="14" viewBox="0 0 24 28"><path d="M12 0a10 10 0 0 0-10 10c0 8 10 18 10 18s10-10 10-18A10 10 0 0 0 12 0zm0 14a4 4 0 1 1 0-8 4 4 0 0 1 0 8z" fill="var(--pink)"/></svg><span>418 Palm Crest Ave, Orlando, Florida</span></div>
      <div class="contact-line"><svg width="12" height="12" viewBox="0 0 24 24"><path fill="var(--pink)" d="M6.6 10.8a15 15 0 0 0 6.6 6.6l2.2-2.2c.3-.3.7-.4 1-.2 1.1.4 2.3.6 3.6.6.6 0 1 .4 1 1V20c0 .6-.4 1-1 1A17 17 0 0 1 3 4c0-.6.4-1 1-1h3.5c.6 0 1 .4 1 1 0 1.3.2 2.5.6 3.6.1.3 0 .7-.2 1z"/></svg><span>321-555-0142</span></div>
      <div class="contact-line"><svg width="12" height="12" viewBox="0 0 24 24"><circle cx="12" cy="12" r="10" fill="none" stroke="var(--pink)" stroke-width="2"/><path d="M2 12h20M12 2c4 4 4 16 0 20M12 2c-4 4-4 16 0 20" fill="none" stroke="var(--pink)" stroke-width="1.5"/></svg><span>wellspringcrest.org</span></div>
    </div>
    <div>
      <h5>SERVICE</h5>
      <ul><li>Hepatitis C Medical Care</li><li>HIV Medical Care</li><li>PREP</li><li>PEP</li><li>STI Testing and Treatment</li><li>Transportation Services</li></ul>
    </div>
    <div>
      <h5>NEWSLETTER</h5>
      <p>Lorem Ipsum is placeholder text commonly used in the graphic.</p>
      <div class="news-input">Enter Your Mail ID</div>
      <a class="btn" style="font-size:12px;padding:8px 18px">Subscribe Now</a>
    </div>
  </div>
  <div class="socials"><span></span><span></span><span></span><span></span></div>
  <div class="footer-rule"></div>
  <p class="copyright">© 2021 Wellspring Crest. All rights reserved.</p>
</footer>

</body>
</html>
```